Branding Package, Velmont Orthodontics
business card, letterhead, envelope, folder
Branding Package, Velmont Orthodontics -
Creative Brief
Bright & Fun-filled
Marcus J. Pellow
Orthodontist
4172 Birchfield Avenue #314 Allentown, PA 18109
info@velmontortho.example
www.velmontortho.example
I would like the logo towards the top of the card. Please add the words "Specializing in Braces for Children and Adults" or "Dr. Marcus J. Pellow" I'd like to see the bottom half of the card in a darker color with white lettering (I think a smile curve line separating the top and the bottom colors would look good). On the front please include our phone, fax, website, and address. Please include the NDB logo in the bottom right corner. All colors must match the current website www.quillsmile.example
Please use a shadow of the tooth portion of the logo with www.velmontortho.example in bold centered on the card...all colors must match the current website: www.quillsmile.example

```html
<!DOCTYPE html>
<html lang="en">
<head>
<meta charset="utf-8">
<title>Velmont Orthodontics – Stationery Concepts</title>
<link href="https://fonts.googleapis.com/css2?family=Montserrat:wght@400;600;800&display=swap" rel="stylesheet">
<style>
:root{
  --stage:#3b3b3d;
  --navy:#0d2c57;
  --deep:#123f72;
  --blue:#1b6fb0;
  --cyan:#27c2d6;
  --ice:#5fd6e4;
  --white:#ffffff;
  --ink:#4a4f57;
  --label:#8a8d92;
}
*{box-sizing:border-box;margin:0;padding:0}
html,body{width:1200px;height:355px;overflow:hidden;background:var(--stage);font-family:"Montserrat",Arial,sans-serif}
.canvas{position:relative;width:1200px;height:355px}
.abs{position:absolute}

.brand{display:flex;align-items:center;gap:6px;color:var(--cyan);font-weight:800;line-height:1.05;white-space:nowrap}
.brand .dot{width:10px;height:10px;border-radius:50%;background:var(--cyan);flex:none}

.hero{left:24px;top:30px;font-size:20px;letter-spacing:.5px;gap:10px}
.hero .dot{width:30px;height:30px}
.title{left:62px;top:86px;color:var(--cyan);font-size:13px;font-weight:600}

.card{width:146px;height:78px;overflow:hidden}
.label{color:var(--label);font-size:6px;text-align:center;width:146px}

.card-front{left:19px;top:162px;background:linear-gradient(160deg,var(--blue),var(--navy))}
.card-info{left:175px;top:162px;background:var(--white)}
.card-web{left:19px;top:258px;background:linear-gradient(160deg,var(--deep),var(--navy))}
.card-light{left:175px;top:258px;background:linear-gradient(160deg,var(--ice),var(--cyan))}
.card svg{position:absolute;left:0;bottom:0}
.card .brand{position:absolute;font-size:9px}
.card .web{position:absolute;width:100%;text-align:center;top:36px;font-size:6px;font-weight:600;color:var(--white)}
.name{position:absolute;right:8px;top:6px;font-size:5px;color:var(--ink);text-align:right;line-height:1.35}
.name b{font-size:6px;color:var(--deep)}
.contact{position:absolute;right:8px;bottom:5px;font-size:4px;color:var(--white);text-align:right;line-height:1.4}

.letterhead{left:331px;top:42px;width:210px;height:296px;background:var(--white);overflow:hidden}
.letterhead .brand{position:absolute;left:12px;top:14px;font-size:7px}
.letterhead .addr{position:absolute;right:12px;top:12px;font-size:4px;color:var(--ink);line-height:1.5;text-align:right}
.letterhead .faint{position:absolute;left:0;width:100%;top:130px;text-align:center;font-size:13px;font-weight:800;color:#eef1f4}
.letterhead svg{position:absolute;left:0;bottom:0}

.env-back{left:566px;top:120px;width:198px;height:120px;background:var(--white)}
.env-back svg{position:absolute;left:0;top:0}
.env-back .brand{position:absolute;left:72px;top:40px;font-size:5px}
.env-front{left:566px;top:276px;width:198px;height:62px;background:var(--white);overflow:hidden}
.env-front .brand{position:absolute;left:8px;top:8px;font-size:7px}
.env-front .addr{position:absolute;left:20px;top:20px;font-size:3.5px;color:var(--ink);line-height:1.4}
.env-front svg{position:absolute;left:0;bottom:0}
.lbl-eb{left:566px;top:243px;width:198px}
.lbl-ef{left:566px;top:341px;width:198px}

.folder-left{left:776px;top:42px;width:196px;height:306px;background:linear-gradient(90deg,var(--blue) 0%,var(--navy) 70%,var(--deep) 100%)}
.folder-right{left:972px;top:42px;width:216px;height:306px;background:var(--white);overflow:hidden}
.folder-right svg{position:absolute;left:0;top:0}
.folder-right .brand{position:absolute;left:62px;top:160px;font-size:11px}
.tagline{position:absolute;right:14px;top:200px;font-size:7px;font-weight:600;color:var(--deep);text-align:right;line-height:1.4}
.pocket-mark{position:absolute;left:96px;top:282px;width:14px;height:14px;border-radius:50%;background:var(--white);opacity:.85}
</style>
</head>
<body>
<main class="canvas">

  <div class="abs brand hero"><span class="dot"></span><span>VELMONT<br>ORTHODONTICS</span></div>
  <p class="abs title">Stationary Concepts</p>

  <section class="abs card card-front">
    <div class="brand" style="left:22px;top:30px"><span class="dot"></span><span>VELMONT<br>ORTHODONTICS</span></div>
  </section>
  <p class="abs label" style="left:19px;top:243px">Business Card Front</p>

  <section class="abs card card-info">
    <div class="brand" style="left:6px;top:8px;font-size:7px"><span class="dot" style="width:7px;height:7px"></span>VELMONT</div>
    <div class="name"><b>Marcus J. Pellow</b><br>Orthodontist</div>
    <svg width="146" height="44" viewBox="0 0 146 44"><path d="M0 12 Q73 34 146 4 L146 44 L0 44Z" fill="var(--cyan)"/><path d="M0 18 Q73 40 146 10 L146 44 L0 44Z" fill="var(--deep)"/></svg>
    <div class="contact">4172 Birchfield Avenue #314, Allentown, PA 18109<br>P (610) 555-0142 · F (610) 555-0143<br>www.velmontortho.example</div>
  </section>
  <p class="abs label" style="left:175px;top:243px">Business Card Back</p>

  <section class="abs card card-web"><p class="web">www.velmontortho.example</p></section>
  <p class="abs label" style="left:19px;top:339px">Card Back Option</p>

  <section class="abs card card-light"><p class="web">www.velmontortho.example</p></section>
  <p class="abs label" style="left:175px;top:339px">Card Back Alternate</p>

  <section class="abs letterhead">
    <div class="brand"><span class="dot" style="width:7px;height:7px"></span>VELMONT ORTHODONTICS</div>
    <div class="addr">4172 Birchfield Avenue #314<br>Allentown, PA 18109<br>info@velmontortho.example</div>
    <div class="faint">VELMONT</div>
    <svg width="210" height="40" viewBox="0 0 210 40"><path d="M0 22 Q110 44 210 6 L210 40 L0 40Z" fill="var(--cyan)"/><path d="M0 28 Q110 46 210 16 L210 40 L0 40Z" fill="var(--deep)"/></svg>
  </section>

  <section class="abs env-back">
    <svg width="198" height="120" viewBox="0 0 198 120"><path d="M0 0 L99 62 L198 0" fill="none" stroke="#d8dde3" stroke-width="1"/><path d="M0 120 L80 58 M198 120 L118 58" stroke="#e6e9ed" stroke-width="1"/></svg>
    <div class="brand"><span class="dot" style="width:5px;height:5px"></span>VELMONT</div>
  </section>
  <p class="abs label lbl-eb">Envelope Back</p>

  <section class="abs env-front">
    <div class="brand"><span class="dot" style="width:7px;height:7px"></span>VELMONT ORTHODONTICS</div>
    <div class="addr">4172 Birchfield Avenue #314<br>Allentown, PA 18109</div>
    <svg width="198" height="14" viewBox="0 0 198 14"><path d="M0 10 Q100 16 198 2 L198 14 L0 14Z" fill="var(--deep)"/></svg>
  </section>
  <p class="abs label lbl-ef">Envelope Front</p>

  <section class="abs folder-left"></section>
  <section class="abs folder-right">
    <svg width="216" height="306" viewBox="0 0 216 306"><path d="M0 0 L0 40 Q6 130 0 306 L0 306Z" fill="var(--deep)"/><path d="M0 250 Q108 232 216 256 L216 306 L0 306Z" fill="var(--deep)"/><path d="M0 250 Q108 228 216 250" fill="none" stroke="var(--cyan)" stroke-width="2"/></svg>
    <div class="brand"><span class="dot"></span><span>VELMONT<br>ORTHODONTICS</span></div>
    <p class="tagline">Incredible smiles<br>Exceptional service<br>Specialist care</p>
    <span class="pocket-mark"></span>
  </section>

</main>
</body>
</html>
```